Acupuncture business needs business card design

I need a business card for an acupuncture clinic called "Summit Wellpath"
It will need the following details:
My name: Marcus Thelwick
Acupuncturist
Member KPTG
BVF Treatment Provider
Ph numbers: 482 1358 027 514 3820
Email: marcus@swpath.example.nz
On the back it will need a table with 2 columns for appointments, one column for time and one for date.

Industry/Entity Type

Clinic

Contact Information for Business Card

Marcus Thelwick
Acupuncturist
Member KPTG
BVF Treatment Provider
Email: marcus@swpath.example.nz

Requirements
Must have
• Marcus Thelwick
• Acupuncturist
• Member KPTG
• BVF Treatment Provider
• Ph numbers: 482 1358 027 514 3820
• Email: marcus@swpath.example.nz
• On the back it will need a table with 2 columns for appointments, one column for time and one for date.

```html
<!DOCTYPE html>
<html lang="en">
<head>
<meta charset="utf-8">
<title>Summit Wellpath – Business Card</title>
<link rel="stylesheet" href="https://fonts.googleapis.com/css2?family=Roboto:wght@400;500&family=Roboto+Condensed:wght@400;700&display=swap">
<style>
  :root {
    --brand-blue: #13b0e0;
    --frame-teal: #147e95;
    --row-cyan: #d3f6f8;
    --rule-dark: #1b2a33;
    --ink: #1e1e1e;
    --white: #ffffff;
    --backdrop: #ecebe8;
    --wood-dark: #5a3a22;
    --wood-light: #9a6a43;
  }
  * { box-sizing: border-box; margin: 0; padding: 0; }
  html, body { width: 1200px; height: 400px; overflow: hidden; }
  body { background: var(--backdrop); position: relative; font-family: "Roboto Condensed", "Arial Narrow", sans-serif; }

  .card { position: absolute; top: 30px; width: 578px; height: 340px; overflow: hidden; }
  .card-front { left: 10px; background: var(--white); }
  .card-back { left: 612px; background: var(--frame-teal); }
  .card svg.shapes { position: absolute; inset: 0; }

  .brand { position: absolute; display: flex; align-items: center; }
  .brand-mark { border-radius: 50%; border: 4px solid var(--brand-blue); flex: none; }
  .brand-name { font-family: "Roboto", sans-serif; font-weight: 500; color: var(--brand-blue); white-space: nowrap; }
  .card-front .brand { left: 32px; top: 22px; gap: 22px; }
  .card-front .brand-mark { width: 50px; height: 50px; }
  .card-front .brand-name { font-size: 50px; line-height: 1; letter-spacing: -0.5px; }

  .credentials { position: absolute; left: 359px; top: 112px; font-size: 17px; line-height: 20px; color: var(--ink); }
  .practitioner { position: absolute; left: 293px; top: 182px; color: var(--white); }
  .practitioner-name { font-weight: 700; font-size: 20px; line-height: 24px; }
  .practitioner-role { font-size: 17px; line-height: 22px; color: var(--ink); }
  .contact-list { list-style: none; margin-top: 14px; font-size: 16px; color: var(--ink); }
  .contact-list li { display: flex; align-items: center; gap: 8px; height: 21px; }
  .contact-list svg { width: 15px; height: 15px; flex: none; }

  .reminder { position: absolute; left: 8px; top: 8px; width: 562px; height: 324px; }
  .reminder-panel { position: absolute; inset: 0 0 64px 0; background: var(--brand-blue); }
  .reminder-title { position: absolute; top: 13px; width: 100%; text-align: center; color: var(--white); font-weight: 700; font-size: 23px; }
  .column-label { position: absolute; top: 56px; color: var(--white); font-size: 18px; }
  .column-label.time { left: 120px; }
  .column-label.date { left: 400px; }
  .appointment-table { position: absolute; left: 0; top: 80px; width: 562px; height: 180px; border-collapse: collapse; }
  .appointment-table td { background: var(--row-cyan); border-bottom: 2.5px solid var(--rule-dark); height: 22.5px; }
  .appointment-table tr:first-child td { border-top: 2px solid var(--rule-dark); }
  .appointment-table td + td { border-left: 2.5px solid var(--rule-dark); }
  .reminder-footer { position: absolute; left: 0; right: 0; bottom: 0; height: 64px; background: var(--white); display: flex; justify-content: center; align-items: center; }
  .reminder-footer .brand { position: static; gap: 12px; }
  .reminder-footer .brand-mark { width: 28px; height: 28px; border-width: 3px; }
  .reminder-footer .brand-name { font-size: 28px; }
</style>
</head>
<body>

<section class="card card-front">
  <svg class="shapes" width="578" height="340" viewBox="0 0 578 340" aria-hidden="false">
    <defs>
      <linearGradient id="wood-tone" x1="0" y1="0" x2="1" y2="1">
        <stop offset="0" stop-color="var(--wood-light)"/>
        <stop offset="1" stop-color="var(--wood-dark)"/>
      </linearGradient>
    </defs>
    <path class="blue-band" d="M0,110 C220,70 400,230 578,175 L578,340 L0,340Z" fill="var(--brand-blue)"/>
    <path class="accent-line" d="M0,97 C220,58 400,218 578,162" fill="none" stroke="var(--brand-blue)" stroke-width="3"/>
    <path class="photo-area" role="img" aria-label="Photo of acupuncture needles and a brass medallion on dark wood"
          d="M0,100 C90,86 180,92 250,120 C266,180 262,260 236,340 L0,340Z" fill="url(#wood-tone)"/>
  </svg>

  <div class="brand">
    <span class="brand-mark"></span>
    <span class="brand-name">Summit Wellpath</span>
  </div>

  <p class="credentials">Member KPTG<br>BVF Treatment Provider</p>

  <div class="practitioner">
    <p class="practitioner-name">Marcus Thelwick</p>
    <p class="practitioner-role">Acupuncturist</p>
    <ul class="contact-list">
      <li>
        <svg viewBox="0 0 16 16" aria-hidden="true"><path d="M1 6c0-2 3-3 7-3s7 1 7 3v1h-3V5.5H4V7H1z M3 8h10l1 6H2z" fill="var(--ink)"/></svg>
        482.1358.
      </li>
      <li>
        <svg viewBox="0 0 16 16" aria-hidden="true"><rect x="4" y="1" width="8" height="14" rx="1.5" fill="none" stroke="var(--ink)" stroke-width="1.5"/><circle cx="8" cy="12.5" r="0.9" fill="var(--ink)"/></svg>
        027.514.3820
      </li>
      <li>
        <svg viewBox="0 0 16 16" aria-hidden="true"><rect x="1" y="3" width="14" height="10" fill="none" stroke="var(--ink)" stroke-width="1.2"/><path d="M1 3l7 6 7-6" fill="none" stroke="var(--ink)" stroke-width="1.2"/></svg>
        marcus@swpath.example.nz
      </li>
    </ul>
  </div>
</section>

<section class="card card-back">
  <div class="reminder">
    <div class="reminder-panel">
      <h2 class="reminder-title">Appointment Reminder</h2>
      <span class="column-label time">Time:</span>
      <span class="column-label date">Date:</span>
    </div>
    <table class="appointment-table">
      <tr><td></td><td></td></tr>
      <tr><td></td><td></td></tr>
      <tr><td></td><td></td></tr>
      <tr><td></td><td></td></tr>
      <tr><td></td><td></td></tr>
      <tr><td></td><td></td></tr>
      <tr><td></td><td></td></tr>
      <tr><td></td><td></td></tr>
    </table>
    <div class="reminder-footer">
      <div class="brand">
        <span class="brand-mark"></span>
        <span class="brand-name">Summit Wellpath</span>
      </div>
    </div>
  </div>
</section>

</body>
</html>
```